Massage-Creme label for a young pharmacy

We are a young pharmacy which is part of a big union. We developed for a customer a very good massage creme with aloe vera, coconut oil, and many more advantages and as well a massage jelly. All we need is a good and affordable label which is beatiful and helps us to promote our product. As we want to develop further products, it would be very cool to have a corporate label for all upcoming products.

Target Market(s)

professional masseurs and physiotherapists

Industry/Entity Type

Health And Wellness

Font styles to use
Sans Serif
Decorative

Colors

Designer to choose colors to be used in the design.

Requirements
Must have
• Professionally looking design (but I'm sure you are doing so... :-)
Nice to have
• Label can have any shape. What you see is just a bad label with corresponding sizes, so you can imagine how it would look like in the final state.
Should not have
• If possible, the label should not be completely black (although it might look cool) as we are printing it on our own Varnick tq318-dm and black is difficult to print (and very costy).

```html
<!DOCTYPE html>
<html lang="de">
<head>
<meta charset="utf-8">
<title>Massage-Crème Etikett</title>
<link href="https://fonts.googleapis.com/css2?family=Roboto:wght@400;500&family=Mrs+Saint+Delafield&display=swap" rel="stylesheet">
<style>
  :root {
    --stage: #e9ecef;
    --green-light: #c2d957;
    --green-mid: #7fb83f;
    --green-deep: #3f8f2f;
    --white: #ffffff;
    --ink: #1d1d1d;
    --badge-red: #e0312b;
  }
  html, body { margin: 0; padding: 0; overflow: hidden; }
  body {
    width: 1200px; height: 900px;
    background: var(--stage);
    font-family: "Roboto", sans-serif;
    position: relative;
  }
  .label {
    position: absolute; left: 60px; top: 10px;
    width: 1080px; height: 880px;
    background: linear-gradient(160deg, var(--green-light) 0%, var(--green-mid) 45%, var(--green-deep) 100%);
    overflow: hidden;
  }
  .front { position: absolute; left: 0; top: 0; width: 540px; height: 880px; }
  .front-frame {
    position: absolute; left: 76px; top: 240px; width: 380px; height: 604px;
    border: 3px solid var(--white); box-sizing: border-box;
  }
  .title-disc {
    position: absolute; left: 74px; top: 4px; width: 392px; height: 392px;
    border-radius: 50%; background: var(--white);
  }
  .product-name {
    position: absolute; left: 74px; top: 100px; width: 392px; text-align: center;
    font-family: "Mrs Saint Delafield", cursive; font-size: 82px; line-height: 1;
    color: var(--ink); transform: rotate(-4deg);
  }
  .variant {
    position: absolute; left: 100px; top: 226px; width: 344px;
    display: flex; align-items: center; gap: 14px;
    font-size: 14px; color: var(--ink); letter-spacing: 0.3px; white-space: nowrap;
  }
  .variant::before, .variant::after { content: ""; flex: 1; height: 2px; background: var(--ink); }
  .badge { position: absolute; left: 88px; top: 414px; width: 150px; height: 84px; }
  .ingredient-art {
    position: absolute; left: 90px; top: 480px; width: 340px; height: 330px;
    border-radius: 20px;
    background: radial-gradient(circle at 60% 55%, #f3ead0 0%, #b88a5a 28%, #6fae4a 55%, rgba(80,150,60,0) 80%);
  }
  .back {
    position: absolute; left: 600px; top: 0; width: 390px; height: 880px;
    color: var(--white); text-align: center;
  }
  .back p { margin: 0; position: absolute; left: 0; width: 100%; font-size: 14px; line-height: 1.25; }
  .claim-intro { top: 82px; }
  .claim-aloe { top: 154px; }
  .claim-energy { top: 244px; }
  .claim-ph { top: 296px; }
  .ph-rule { position: absolute; left: 64px; top: 320px; width: 270px; height: 2px; background: var(--white); }
  .ph-rule::after { content: ""; position: absolute; left: 128px; top: -3px; width: 8px; height: 8px; border-radius: 50%; background: var(--white); }
  .back p.claim-quality { top: 368px; font-size: 11px; }
  .free-from {
    position: absolute; left: 30px; top: 420px; width: 320px; height: 64px;
    border: 2px solid var(--white); box-sizing: border-box;
    display: flex; align-items: center; justify-content: center;
    font-size: 11px; line-height: 1.25; padding: 0 12px;
  }
  .maker { position: absolute; left: 180px; top: 654px; text-align: left; line-height: 1.1; }
  .maker-name { font-size: 15px; font-weight: 500; color: var(--white); }
  .maker-sub { font-size: 10px; color: var(--white); }
  .maker-dot { display: inline-block; width: 8px; height: 8px; background: var(--white); border-radius: 50%; margin-right: 6px; }
  .batch { position: absolute; left: 14px; top: 706px; text-align: left; font-size: 10px; line-height: 1.3; }
  .back p.ingredients { top: 748px; left: 14px; width: 360px; text-align: left; font-size: 9px; line-height: 1.3; }
  .back p.volume { top: 804px; font-size: 14px; }
</style>
</head>
<body>
  <section class="label" aria-label="Etikett Massage-Crème">
    <div class="front">
      <div class="front-frame"></div>
      <div class="title-disc"></div>
      <div class="product-name">Massage-Crème</div>
      <div class="variant">COCONUT - ALOE VERA</div>
      <svg class="badge" viewBox="0 0 150 84" aria-label="energetisch leitend">
        <polygon fill="var(--white)" stroke="var(--badge-red)" stroke-width="4"
          points="75,4 86,14 102,6 108,20 126,16 126,31 144,34 134,46 146,58 130,62 134,78 116,74 106,84 94,74 75,80 58,72 44,82 38,68 20,72 22,58 4,52 16,42 6,30 24,28 24,14 42,18 50,6 64,14"/>
        <text x="75" y="40" text-anchor="middle" font-family="Roboto, sans-serif" font-size="15" fill="var(--ink)">energetisch</text>
        <text x="75" y="57" text-anchor="middle" font-family="Roboto, sans-serif" font-size="15" fill="var(--ink)">leitend !</text>
      </svg>
      <div class="ingredient-art" role="img" aria-label="Aloe-Vera-Blätter, halbe Kokosnuss und Ölfläschchen"></div>
    </div>

    <div class="back">
      <p class="claim-intro">Hochwertige und sehr hautschonende Emulsion mit hervorragendem Gleitverhalten für die professionelle Massage.</p>
      <p class="claim-aloe">Hilft durch den hohen Gehalt an Aloe Vera-Gel (50%), die Feuchtigkeit der Haut zu erhalten und schützt durch die Zugabe von Panthenol (= Provitamin B5) und Allantoin vor Hautreizungen.</p>
      <p class="claim-energy">Speziell für die (bio-)energetische Massage entwickelt.</p>
      <p class="claim-ph">pH-neutral für die Haut (pH-Wert = 5.5)</p>
      <div class="ph-rule"></div>
      <p class="claim-quality">Bei der Entwicklung unserer Produkte legen wir grössten Wert auf gute Verträglichkeit und hochwertige Rohstoffe.</p>
      <div class="free-from">Dieses Produkt ist frei von Parabenen, Mineralölen (Paraffin/Vaseline), Silikonen, Farbstoffen und Mikroplastik (Acrylate).</div>
      <div class="maker">
        <div class="maker-name"><span class="maker-dot"></span>Kelvora</div>
        <div class="maker-sub">Apotheke Dr. Lindqvar</div>
      </div>
      <div class="batch">Exp: 03.2021<br>Lot: 913015/A</div>
      <p class="ingredients">Zus: water (aqua), cetearyl isononanoate, ethylhexyl stearate, cocos nucifera (coconut) oil, butyrospermum parkii butter, glyceryl stearate citrate, cetearyl alcohol, phenoxyethanol, aloe barbadensis leaf juice, panthenol, sodium chloride, xanthan gum, allantoin, citric acid, parfum.</p>
      <p class="volume">℮ 1000 ml</p>
    </div>
  </section>
</body>
</html>
```